Tilda and Rook Competition Poster.

Hi Deigners,
I need to help to design a poster for a competition.
Details for competition is exactly the same as my previous design but simply change the name to TILDA & ROOK.
Competition will start : 1st AUGUST 2017
Competion end : 31st AUGUST 2017
Poster name: TILDA & ROOK BREEZE COMPETITION
Poster Description:
WIN a $100 Food Voucher
Share your photos on TOWNSQUARE or PICTURA to WIN.
To Enter, Simply:
1. Like our Townsquare page or follow us on Pictura
2. Take an original photo of any item(s) of our food
3. Post your photo(s) to our Townsquare page or Pictura page, must use hashtags #tildaandrook #tildaandbreeze
4. Be as creative as you'd like, and the TWO BEST photos voted by the Tilda and Rook team will receive a $100 Food Voucher.
I've also attached the Terms & Conditions, Please Copy and Paste these terms but must replace it with the updated details.
Good Luck everyone

```html
<!DOCTYPE html>
<html lang="en">
<head>
<meta charset="utf-8">
<title>Tilda and Rook Breeze Competition</title>
<link rel="stylesheet" href="https://fonts.googleapis.com/css2?family=Anton&family=Open+Sans:wght@400;600;700&display=swap">
<style>
  :root {
    --orange: #f26a2b;
    --orange-light: #f7a27a;
    --orange-deep: #ee5a1c;
    --ink: #1f1f1f;
    --white: #ffffff;
    --paper: #ffffff;
    --bar-dark: #3a3a3a;
    --stage: #ececec;
  }
  * { margin: 0; padding: 0; box-sizing: border-box; }
  html, body { width: 1200px; height: 800px; overflow: hidden; }
  body { background: var(--stage); font-family: "Open Sans", sans-serif; position: relative; }

  .page { position: absolute; top: 64px; width: 476px; height: 672px; overflow: hidden; box-shadow: 0 4px 10px rgba(0,0,0,.25); }
  .poster { left: 110px; background: radial-gradient(ellipse at 50% 28%, var(--orange-light) 0%, var(--orange) 55%, var(--orange-deep) 100%); color: var(--white); }
  .terms { left: 614px; background: var(--paper); color: var(--ink); }

  .brand-box { position: absolute; background: var(--white); display: flex; align-items: center; justify-content: center; text-align: center; }
  .brand-name { font-family: "Open Sans", sans-serif; font-weight: 700; color: var(--orange); line-height: 1.1; }
  .poster .brand-box { left: 372px; top: 34px; width: 90px; height: 122px; }
  .poster .brand-name { font-size: 17px; }
  .terms .brand-box { left: 388px; top: 8px; width: 71px; height: 96px; }
  .terms .brand-name { font-size: 14px; }

  .title { position: absolute; left: 38px; top: 28px; font-family: "Anton", sans-serif; font-weight: 400; line-height: 1.05; letter-spacing: .5px; text-shadow: 1px 2px 2px rgba(0,0,0,.25); white-space: nowrap; }
  .title-top { display: block; font-size: 36px; }
  .title-bottom { display: block; font-size: 48px; }
  .prize { position: absolute; left: 39px; top: 136px; font-size: 23px; font-weight: 600; color: var(--ink); white-space: nowrap; }
  .dates { position: absolute; left: 38px; top: 170px; font-size: 15px; font-weight: 700; line-height: 23px; white-space: nowrap; }

  .dish { position: absolute; left: 26px; top: 220px; width: 420px; height: 268px; border-radius: 50%;
    background: radial-gradient(ellipse at 50% 45%, #5a7a2e 0%, #6b4a2e 45%, #8a4a22 62%, #dfe6e2 72%, #c9d3cf 100%); }

  .share { position: absolute; left: 36px; top: 498px; font-size: 25px; font-weight: 600; line-height: 32px; white-space: nowrap; }
  .steps-heading { position: absolute; left: 38px; top: 566px; font-size: 18px; font-weight: 600; color: var(--ink); }
  .steps { position: absolute; left: 38px; top: 589px; width: 420px; list-style: none; font-size: 10px; line-height: 12px; }
  .steps li { position: relative; padding-left: 10px; }
  .steps li::before { content: ""; position: absolute; left: 0; top: 5px; width: 3px; height: 3px; border-radius: 50%; background: var(--white); }
  .hashtags { font-weight: 700; }

  .hero { position: absolute; left: 0; top: 0; width: 476px; height: 360px; }
  .terms-heading { position: absolute; left: 20px; top: 376px; font-size: 23px; line-height: 28px; font-weight: 600; letter-spacing: .2px; white-space: nowrap; padding: 0 24px 2px 0; border-bottom: 2px solid var(--orange); }
  .terms-body { position: absolute; left: 24px; top: 422px; width: 440px; font-size: 8.2px; line-height: 11px; }
  .terms-body p { margin-bottom: 10.5px; }
  .footer-bar { position: absolute; left: 0; bottom: 0; width: 476px; height: 7px; background: linear-gradient(90deg, var(--orange) 0 398px, var(--bar-dark) 398px); }
</style>
</head>
<body>

<section class="page poster">
  <h1 class="title"><span class="title-top">TILDA &amp; ROOK BREEZE</span><span class="title-bottom">COMPETITION</span></h1>
  <div class="brand-box"><span class="brand-name">Kettle<br>Lane</span></div>
  <p class="prize">WIN a $100 Food Voucher</p>
  <p class="dates">Competition will start : 1st AUGUST 2017<br>Competion end : 31st AUGUST 2017</p>
  <div class="dish" role="img" aria-label="Bowl of beef noodle soup with herbs, bean sprouts and meatballs"></div>
  <p class="share">Share your photos on<br>TOWNSQUARE or PICTURA to WIN</p>
  <h2 class="steps-heading">To Enter, Simply:</h2>
  <ul class="steps">
    <li>Like our Townsquare page or follow us on Pictura</li>
    <li>Take an original photo of any item(s) of our food</li>
    <li>Post your photo(s) to our Townsquare page or Pictura page, must use hashtags<br><span class="hashtags">#tildaandrook #tildaandbreeze</span></li>
    <li>Be as creative as you'd like, and the TWO BEST photos voted by the Tilda and Rook team will receive a <strong>$100 Food Voucher</strong>.</li>
  </ul>
</section>

<section class="page terms">
  <svg class="hero" viewBox="0 0 476 360">
    <defs>
      <linearGradient id="tableTone" x1="0" y1="0" x2="1" y2="1">
        <stop offset="0" stop-color="#d9cdb8"/>
        <stop offset="1" stop-color="#b8a98f"/>
      </linearGradient>
    </defs>
    <path d="M0 0 H476 V300 Q250 390 0 255 Z" fill="var(--orange)"/>
    <path d="M0 0 H476 V278 Q250 378 0 250 Z" fill="url(#tableTone)" role="img" aria-label="Two diners photographing plates of food and coffee on a table with their phones"/>
  </svg>
  <div class="brand-box"><span class="brand-name">Kettle<br>Lane</span></div>
  <h2 class="terms-heading">TERMS &amp; CONDITIONS</h2>
  <div class="terms-body">
    <p>The competition opens 9:00am on Monday 1st February and closes at 11:59pm Sunday 28th February. Judging of entries will be completed at the Kettle Lane Elm St store by 9:00pm the following Tuesday and the winners name e entry will be announced visa Townsquare and Pictura post at 12:00pm Wednesday 2. March 2016.</p>
    <p>All entries must not have been used in previous Kettle Lane competitions and the number of entries an Eligible Entrant may send is not hooted, provided each entry is different and tagged correctly. This is a game of skill. Each entry will be individually judged, based upon individual creative merit. The entry image must be the Eligible Entrant's original piece. Employees of Kettle Lane and immediate families are ineligible to enter the competition.</p>
    <p>The prize is valued at $100 per winner, to be used within 6 months of receipt. The prize is not transferable &amp; cannot be converted to cash.</p>
    <p>The Promoter is not liable for any loss or damage which is suffered or incurred by any person, including but not limited to indirect or consequential loss, or for personal injury suffered or sustained during the course of accepting or using the prize, except for any liability which cannot be excluded by law. By entering the competition, each entrant acknowledges their entry content may be used for printing, broadcast, publicity and promotional purposes, including but not limited to the Promoter's websites and social media accounts without compensation.</p>
    <p>The Promoter is Kettle Lane Pty Ltd (ABN 11 204 583 716) Shop 4/ 12 Harbour Row Greenvale NSW 2199. Ground Floor, Shop 1/ 90 Elm St, Sydney NSW 2000.</p>
  </div>
  <div class="footer-bar"></div>
</section>

</body>
</html>
```